My dynamic new collection of short plays needs an eye catching web-based ad!

I am buying ad space on a theater magazine's website with these specs for a new book. The ad will run for a few months. I have the book cover - which will be the main image, but need the ad designed with quotes and the publisher's logo. Here are the specs:
230 pixels wide x 250 pixels high
72 dpi

Target Market(s)

Theater artists and theater educators

Industry/Entity Type

Theater / Education

Font styles to use
Sans Serif
Other font styles liked:
• Please use fonts that match the book cover. I'm including an ad that is currently on the website where I will be advertising. It is not the size that I'm going for, but it contains the elements that I want. I'm also including an image of the logo of the publisher, and I have other versions of this logo (other formats / larger size) that I can deliver if needed.

Requirements
Must have
• Simple compelling image with a quote from the book and a link to the publisher website. A compelling quote (or two) from the book jacket. The name and logo of the publisher.
Nice to have
• Some eye catching color to compliment the beautiful cover design
Should not have
• Too much busy-ness in the image or the presentation.

```html
<!DOCTYPE html>
<html lang="en">
<head>
<meta charset="utf-8">
<title>Some Quiet Plays to Mend the World – Book Ad</title>
<link href="https://fonts.googleapis.com/css2?family=Montserrat:ital,wght@0,600;0,700;0,800;1,800&display=swap" rel="stylesheet">
<style>
  :root {
    --page-bg: #d9d9d9;
    --ink: #222222;
    --accent-blue: #1a8cff;
    --title-box: #13317f;
    --title-text: #eaf3ff;
    --navy-deep: #0b1a5a;
    --panel-top: #f3f7fc;
    --panel-mid: #5b8fd6;
    --panel-low: #1d46a8;
    --frame-line: #ffffff;
    --footer-bg: #ffffff;
  }
  * { margin: 0; padding: 0; box-sizing: border-box; }
  html, body { width: 1200px; height: 1200px; overflow: hidden; background: var(--page-bg); }
  body { font-family: "Montserrat", sans-serif; position: relative; }

  .ad {
    position: absolute; left: 136px; top: 95px;
    width: 930px; height: 1010px; overflow: hidden;
    background: linear-gradient(180deg, var(--panel-top) 0px, #dfeaf8 200px, var(--panel-mid) 380px, var(--panel-low) 620px, var(--navy-deep) 866px);
  }
  .ad > * { position: absolute; }

  .author-kicker {
    top: 50px; left: 0; width: 930px; text-align: center;
    font-weight: 800; font-size: 41px; letter-spacing: 1px; color: var(--accent-blue);
  }
  .kicker-rule { top: 74px; height: 1.5px; background: var(--ink); }
  .kicker-rule.left { left: 78px; width: 177px; }
  .kicker-rule.right { left: 674px; width: 179px; }

  .title-line {
    top: 113px; left: 0; width: 930px; text-align: center;
    font-weight: 800; font-size: 60px; letter-spacing: 1px; color: var(--ink); line-height: 72px;
  }
  .title-box {
    top: 184px; left: 61px; width: 808px; height: 81px; background: var(--title-box);
    color: var(--title-text); font-weight: 800; font-size: 76px; line-height: 81px; text-align: center;
    letter-spacing: 1px;
  }

  .book-cover {
    left: 63px; top: 305px; width: 385px; height: 494px;
    background: radial-gradient(ellipse at 48% 45%, #4fb4ff 0%, #2a6fe0 30%, #1d3fae 62%, #1a2a80 100%);
    clip-path: polygon(43px 59px, 316px 22px, 316px 330px, 385px 333px, 385px 478px, 6px 494px, 6px 420px, 43px 420px);
  }

  .quote-frame { left: 0; top: 0; width: 930px; height: 1010px; pointer-events: none; }
  .quote-mark {
    font-weight: 800; font-size: 120px; line-height: 1; color: var(--accent-blue);
  }
  .quote-mark.first { left: 530px; top: 278px; }
  .quote-mark.second { left: 530px; top: 567px; }

  .quote-text {
    left: 539px; width: 318px;
    color: #ffffff; font-weight: 700; font-size: 16px; line-height: 20.2px;
  }
  .quote-text.first { top: 349px; }
  .quote-text.second { top: 655px; width: 334px; }

  .quote-name {
    right: 83px; text-align: right; color: var(--accent-blue);
    font-weight: 800; font-size: 26px; letter-spacing: 0.3px; line-height: 30px;
  }
  .quote-role {
    right: 83px; text-align: right; color: #ffffff;
    font-weight: 800; font-style: italic; font-size: 19.5px; line-height: 24px;
  }
  .quote-name.first { top: 475px; }
  .quote-role.first { top: 503px; }
  .quote-name.second { top: 758px; }
  .quote-role.second { top: 785px; }

  .accent-band { left: 0; top: 866px; width: 930px; height: 9px; background: var(--accent-blue); }
  .footer { left: 0; top: 875px; width: 930px; height: 135px; background: var(--footer-bg); }
  .footer-lead {
    right: 438px; top: 908px; font-weight: 700; font-size: 33px; color: var(--ink); letter-spacing: 0.5px;
  }
  .footer-divider { left: 506px; top: 905px; width: 2.5px; height: 58px; background: var(--ink); }
  .publisher { left: 524px; top: 900px; display: flex; align-items: center; gap: 12px; }
  .publisher-dot { width: 64px; height: 64px; border-radius: 50%; background: var(--ink); }
  .publisher-name { font-weight: 700; font-size: 17px; color: var(--ink); letter-spacing: 1px; }
</style>
</head>
<body>
  <main class="ad">
    <div class="kicker-rule left"></div>
    <h2 class="author-kicker">MARCUS DALE’S</h2>
    <div class="kicker-rule right"></div>

    <h1 class="title-line">SOME QUIET PLAYS TO</h1>
    <div class="title-box">MEND THE WORLD</div>

    <div class="book-cover" role="img" aria-label="Book cover of Some Quiet Plays to Mend the World, shown as a standing paperback on a stack, with a colourful portrait illustration of the author"></div>

    <svg class="quote-frame" viewBox="0 0 930 1010" aria-hidden="true">
      <g fill="none" stroke="var(--frame-line)" stroke-width="1.5">
        <polyline points="531,315 509,315 509,507 611,507"/>
        <polyline points="600,315 885,315 885,507 858,507"/>
        <polyline points="531,605 509,605 509,792 535,792"/>
        <polyline points="600,605 885,605 885,792 858,792"/>
      </g>
    </svg>

    <div class="quote-mark first">“</div>
    <p class="quote-text first">Marcus Dale’s writing has an underlying, yet profound sadness to it. It is powerful in his work and keys into the inherit loneliness that all human beings experience at one time or another.</p>
    <div class="quote-name first">RAFAEL MOORE</div>
    <div class="quote-role first">Coastal Arts Review</div>

    <div class="quote-mark second">“</div>
    <p class="quote-text second">Marcus provokes us to look more carefully at systems of race and power and our participation in them in ways that linger long after the blackout.</p>
    <div class="quote-name second">NINA HALVORSEN</div>
    <div class="quote-role second">Artistic Director, Lumen Stage</div>

    <div class="accent-band"></div>
    <footer class="footer"></footer>
    <div class="footer-lead">Available now from</div>
    <div class="footer-divider"></div>
    <div class="publisher">
      <span class="publisher-dot"></span>
      <span class="publisher-name">QUIET LANTERN PRESS</span>
    </div>
  </main>
</body>
</html>
```